Property Auctions with Gareth Whitlow

Podcast cover art 3000px by 3000px. Eye catching for a weekly podcast. The words should read Property Auctions (large font) with Gareth Whitlow (smaller font)

I would like the font and colours to be similar to my book, a copy of which I have attached.

Target Market(s)

New and experienced property investors looking to purchase at a property auction

```html
<!DOCTYPE html>
<html lang="en">
<head>
<meta charset="utf-8">
<title>Property Auctions with Gareth Whitlow</title>
<link rel="stylesheet" href="https://fonts.googleapis.com/css2?family=Oswald:wght@700&display=swap">
<style>
  :root {
    --canvas-black: #000000;
    --paper-white: #ffffff;
    --slate: #283236;
    --gold-deep: #d6ad45;
    --gold-mid: #f2dc7c;
    --gold-light: #fffdb5;
    --photo-warm: #c49a68;
    --photo-green: #9aa064;
    --photo-cream: #efe2cf;
    --photo-dark: #4a3428;
  }
  html, body {
    margin: 0;
    padding: 0;
    overflow: hidden;
    background: var(--canvas-black);
  }
  .canvas {
    position: relative;
    width: 1179px;
    height: 1200px;
    background: var(--canvas-black);
    overflow: hidden;
  }
  .cover-art {
    position: absolute;
    left: 149px;
    top: 160px;
    width: 881px;
    height: 880px;
    display: block;
  }
  .title-line {
    position: absolute;
    left: 0;
    width: 862px;
    margin: 0;
    text-align: center;
    font-family: "Oswald", "Arial Narrow", sans-serif;
    font-weight: 700;
    line-height: 1;
    text-transform: uppercase;
    white-space: nowrap;
  }
  .title-main {
    font-size: 124px;
    letter-spacing: -1px;
    filter: drop-shadow(3px 4px 4px rgba(0, 0, 0, 0.55));
  }
  .title-main span {
    background: linear-gradient(90deg, var(--gold-deep) 0%, var(--gold-mid) 30%, var(--gold-light) 50%, var(--gold-mid) 72%, var(--gold-deep) 100%);
    -webkit-background-clip: text;
    background-clip: text;
    color: transparent;
  }
  .title-property { top: 446px; }
  .title-auctions { top: 576px; }
  .host-name {
    top: 727px;
    font-size: 46px;
    color: var(--paper-white);
    text-shadow: 2px 3px 3px rgba(0, 0, 0, 0.6);
  }
</style>
</head>
<body>
<div class="canvas">
  <svg class="cover-art" viewBox="0 0 1422 1422" preserveAspectRatio="none" aria-hidden="false">
    <defs>
      <linearGradient id="goldSweep" x1="0" y1="0" x2="1" y2="0">
        <stop offset="0" stop-color="var(--gold-deep)"/>
        <stop offset="0.55" stop-color="var(--gold-light)"/>
        <stop offset="1" stop-color="var(--gold-mid)"/>
      </linearGradient>
      <linearGradient id="photoTones" x1="0" y1="0" x2="0.6" y2="1">
        <stop offset="0" stop-color="var(--photo-warm)"/>
        <stop offset="0.25" stop-color="var(--photo-green)"/>
        <stop offset="0.5" stop-color="var(--photo-cream)"/>
        <stop offset="0.8" stop-color="var(--photo-warm)"/>
        <stop offset="1" stop-color="var(--photo-dark)"/>
      </linearGradient>
      <clipPath id="photoArea">
        <path d="M657,268 C720,130 800,50 905,0 L1422,0 L1422,1422 L657,1422 Z"/>
      </clipPath>
    </defs>

    <rect class="paper" x="0" y="0" width="1422" height="1422" fill="var(--paper-white)"/>

    <rect class="photo-placeholder" x="0" y="0" width="1422" height="1422"
          fill="url(#photoTones)" clip-path="url(#photoArea)"
          role="img" aria-label="Photo of a small wooden model house on a table with a hand behind it"/>

    <path class="gold-crescent" d="M650,258 C690,130 740,50 780,0 L895,0 C790,55 712,140 652,262 Z" fill="url(#goldSweep)"/>

    <path class="slate-panel" d="M-10,182 C400,130 1100,380 1240,1187 L1240,1440 L-10,1440 Z"
          fill="var(--slate)" stroke="var(--paper-white)" stroke-width="8"/>

    <path class="base-band" d="M110,1422 C400,1180 1000,1000 1422,1268 L1422,1422 Z" fill="var(--paper-white)"/>
    <path class="base-gold" d="M155,1422 C450,1200 1000,1040 1422,1300 L1422,1422 Z" fill="url(#goldSweep)"/>
  </svg>

  <h1 class="title-line title-main title-property"><span>Property</span></h1>
  <p class="title-line title-main title-auctions"><span>Auctions</span></p>
  <p class="title-line host-name">Gareth Whitlow</p>
</div>
</body>
</html>
```